Personal Training, Nutrition and Habit Change

I am looking to create a memorable brand name and logo that describes what I offer..something like, "Bold Oak Daily" or "Kestrel Grove Fitness". I want people to know that they can come to me to elevate their lives through a balance of fitness, good nutrition and mental well-being through meditating, mindfulness and a program of stress relief.

Target Market(s)

Well established individuals who are interested in spending money for their health and well-being and making a long term commitment to themselves.

Industry/Entity Type

Fitness

Contact Information for Business Card

Would like a horizontal card, possibly in black with blue and white lettering with the logo that implies a figure running, moving fast or is agile. Would like a statement on the back about habit change and importance of fitness

Logo Text

Create A Stronger Healthier You or Elevate Your Life and Well Being

Font styles to use
Sans Serif

Colors

Designer to choose colors to be used in the design.

Requirements
Must have
• A strong, powerful name (brand) for my company. Something short, powerful, memorable and relevant. A company motto that describes briefly what I'll help clients achieve, i.e. Create a Stronger Healthier You, etc. A place for my name and multiple credentials with room for contact info of course. On the back, does it make practical sense to describe habit change, achieving balance making commitment to one's health and well being and finding great joy in one's daily life.
Nice to have
• Basically what I said above.
Should not have
• Just show me what you've got!

```html
<!DOCTYPE html>
<html lang="en">
<head>
<meta charset="utf-8">
<title>Kestrel Grove Fitness – Business Card</title>
<link href="https://fonts.googleapis.com/css2?family=Questrial&display=swap" rel="stylesheet">
<style>
  :root {
    --bg: #dcdcdc;
    --card-white: #ffffff;
    --card-black: #141414;
    --brand-blue: #3f7fc6;
    --ink: #111111;
    --paper-text: #ffffff;
  }
  * { margin: 0; padding: 0; box-sizing: border-box; }
  html, body {
    width: 1200px; height: 900px; overflow: hidden;
    background: var(--bg);
    font-family: "Questrial", "Century Gothic", sans-serif;
  }
  .canvas { position: relative; width: 1200px; height: 900px; }
  .card {
    position: absolute; width: 640px; height: 380px;
    border-radius: 26px; overflow: hidden;
    box-shadow: 0 10px 24px rgba(0,0,0,0.25);
  }
  /* front */
  .card-front { left: 60px; top: 50px; background: var(--card-white); color: var(--ink); }
  .brand {
    position: absolute; display: flex; align-items: center; gap: 12px;
  }
  .brand-dot { width: 30px; height: 30px; border-radius: 50%; background: var(--brand-blue); }
  .brand-name { font-size: 30px; letter-spacing: 1px; text-transform: uppercase; }
  .card-front .brand { left: 40px; top: 38px; }
  .card-front .brand-name { color: var(--ink); }
  .holder { position: absolute; left: 40px; top: 112px; }
  .holder-name { font-size: 27px; text-transform: uppercase; letter-spacing: 0.5px; }
  .holder-roles { margin-top: 8px; color: var(--brand-blue); font-size: 15px; line-height: 1.45; text-transform: uppercase; }
  .contact { position: absolute; left: 40px; top: 262px; font-size: 17px; line-height: 1.9; }
  .contact-line { display: flex; align-items: center; gap: 10px; }
  .contact-line svg { width: 18px; height: 18px; fill: var(--ink); }
  .accent-disc {
    position: absolute; right: -110px; bottom: -170px;
    width: 400px; height: 400px; border-radius: 50%;
    background: var(--brand-blue);
  }
  /* back */
  .card-back { left: 500px; top: 470px; background: var(--card-black); color: var(--paper-text); }
  .back-content {
    position: absolute; inset: 0; display: flex; flex-direction: column;
    align-items: center; justify-content: center; gap: 34px;
  }
  .card-back .brand { position: static; }
  .card-back .brand-name { color: var(--paper-text); font-size: 36px; }
  .card-back .brand-dot { width: 36px; height: 36px; }
  .motto { font-size: 20px; letter-spacing: 0.5px; text-transform: uppercase; }
  .motto-accent { color: var(--brand-blue); }
</style>
</head>
<body>
<main class="canvas">
  <section class="card card-front">
    <div class="brand">
      <span class="brand-dot"></span>
      <span class="brand-name">Kestrel Grove Fitness</span>
    </div>
    <div class="holder">
      <p class="holder-name">Dana Whitfield</p>
      <p class="holder-roles">CPT, Nutrition, Yoga Certified<br>Founder &nbsp;|&nbsp; Fitness Professional<br>Habit Change Specialist</p>
    </div>
    <div class="contact">
      <p class="contact-line">
        <svg viewBox="0 0 24 24" aria-hidden="true"><path d="M6.6 10.8a15.1 15.1 0 0 0 6.6 6.6l2.2-2.2a1 1 0 0 1 1-.25 11.4 11.4 0 0 0 3.6.57 1 1 0 0 1 1 1V20a1 1 0 0 1-1 1A17 17 0 0 1 3 4a1 1 0 0 1 1-1h3.5a1 1 0 0 1 1 1c0 1.25.2 2.45.57 3.57a1 1 0 0 1-.25 1z"/></svg>
        555-014-2273
      </p>
      <p class="contact-line">
        <svg viewBox="0 0 24 24" aria-hidden="true"><path d="M2 5h20v14H2zm2 2v.5l8 5 8-5V7zm0 2.8V17h16V9.8l-8 5z"/></svg>
        hello@kestrelgrovefit.com
      </p>
    </div>
    <div class="accent-disc"></div>
  </section>

  <section class="card card-back">
    <div class="back-content">
      <div class="brand">
        <span class="brand-dot"></span>
        <span class="brand-name">Kestrel Grove Fitness</span>
      </div>
      <p class="motto">Create a Stronger Healthier <span class="motto-accent">You</span></p>
    </div>
  </section>
</main>
</body>
</html>
```